Card for invoking rights with police

Our criminal defense law firm is seeking proposals for a design for our card intended for clients to carry with them in their car. Upon being pulled over, they would hand this card to the officer.
Text for the back of the card:
"For Law Enforcement:"
"I will comply with lawful orders but respectfully decline any test or other requests without my attorney. I wish to remain silent, do not consent to searches, and request to speak with my attorney now.
The back of the card should prominently feature the text and the firm logo should be secondary.
Front
Must prominently feature contact info: 503-555-0182. Do not include attorney name, email, phone from the example file. This is intended to be generic for the firm and not tied to an individual lawyer.
Included for design reference: current business card, firm logo.
We intend to use trenvo.com to produce the cards.
Updates
The back of the card should prominently display the text regarding invocation of rights. Please title it "For Law Enforcement".
Target Market(s)
People who have been stopped by police
Contact Information for Business Card
see project description
Look and feel

```html
<!DOCTYPE html>
<html lang="en">
<head>
<meta charset="utf-8">
<title>Rights Card – Front and Back</title>
<link href="https://fonts.googleapis.com/css2?family=Cinzel:wght@500&family=Libre+Baskerville&display=swap" rel="stylesheet">
<style>
  :root {
    --navy: #023254;
    --white: #ffffff;
    --backdrop: #e4e4e4;
    --rule: #7b93a8;
  }
  * { margin: 0; padding: 0; box-sizing: border-box; }
  html, body {
    width: 1125px;
    height: 1200px;
    overflow: hidden;
    background: var(--backdrop);
  }
  .canvas {
    position: relative;
    width: 1125px;
    height: 1200px;
  }
  .card {
    position: absolute;
    left: 150px;
    width: 826px;
    height: 471px;
    padding: 32px 36px;
  }
  .card-front { top: 98px; background: var(--white); }
  .card-back  { top: 631px; background: var(--navy); }

  .panel {
    width: 100%;
    height: 100%;
    display: flex;
    flex-direction: column;
    align-items: center;
  }
  .card-front .panel {
    background: var(--navy);
    justify-content: flex-start;
  }
  .phone-number {
    margin-top: 150px;
    font-family: "Libre Baskerville", serif;
    font-size: 62px;
    letter-spacing: 1px;
    color: var(--white);
  }

  .card-back .panel {
    background: var(--white);
    padding-top: 50px;
  }
  .back-title {
    font-family: "Cinzel", serif;
    font-weight: 500;
    font-size: 45px;
    letter-spacing: 1px;
    color: var(--navy);
    line-height: 1;
  }
  .title-rule {
    display: block;
    margin: 24px 0 18px;
  }
  .rights-statement {
    font-family: "Libre Baskerville", serif;
    font-size: 27px;
    line-height: 38.5px;
    color: #111;
    text-align: center;
    width: 660px;
  }
</style>
</head>
<body>
<main class="canvas">
  <section class="card card-front" aria-label="Card front">
    <div class="panel">
      <p class="phone-number">503-555-0182</p>
    </div>
  </section>

  <section class="card card-back" aria-label="Card back">
    <div class="panel">
      <h1 class="back-title">FOR LAW ENFORCEMENT</h1>
      <svg class="title-rule" width="300" height="2" viewBox="0 0 300 2" aria-hidden="true">
        <defs>
          <linearGradient id="ruleFade" x1="0" x2="1" y1="0" y2="0">
            <stop offset="0" stop-color="#7b93a8" stop-opacity="0"/>
            <stop offset="0.5" stop-color="#7b93a8" stop-opacity="1"/>
            <stop offset="1" stop-color="#7b93a8" stop-opacity="0"/>
          </linearGradient>
        </defs>
        <rect width="300" height="1.5" fill="url(#ruleFade)"/>
      </svg>
      <p class="rights-statement">I will comply with lawful orders but respectfully decline any test or other requests without my attorney.<br>I wish to remain silent, do not consent to searches, and request to speak with my attorney now.</p>
    </div>
  </section>
</main>
</body>
</html>
```